ORBIT Learning League - Coalition for Fair Access in Digital Schooling - Sticker for Laptops, Branding

We need a sticker design for the ORBIT Learning League that we can share at our own events and at exhibitor booths at other events. We have a logo that you can incorporate, but we welcome creative designs. We want something colorful that will stand out - not just the existing logo on a plain white background! We are also including the PixelHive "add-on" project to design an updated/alternative logo/brand as an add-on!

About ORBIT:
Nationally, there are significant disparities in computer science (CS) degree programs and in the computing workforce with respect to race, gender, and intersections thereof. Only 21% of CS graduates identified as women, 3% as Black, and 8.5% as Hispanic. These trends continue in industry; only 24% of tech professionals identify as women, 3.1% as having a disability, 8.8% as Black, and 8% as Hispanic.

The ORBIT Learning League (www.orbitlearningleague.example) is a national alliance of colleges and universities, with a mission to shift practices in college computing departments to advance diversity, equity, and inclusion in computing. Specifically, ORBIT provides training, resources, and community to help college faculty and students to develop as leaders who take action to eliminate barriers to participation for historically excluded groups in computing and to advance diversity, equity, and inclusion in computing.

Typically, college students participating in a ORBIT Learning League chapter will work with K12 teachers in their local communities to provide or enhance learning opportunities for K12 students. These projects are designed to promote persistence and career advancement in computing, by connecting computing to community and societal impacts; reinforcing computing knowledge through teaching and practice; developing professional, entrepreneurial, and creative skills, and developing a network of computing professionals with a shared commitment to diversity, equity, and computing. Faculty participating in ORBIT will typically adopt an inclusive practice within their department and/or engage in research that advances justice-centered computing education and workforce preparation.

An analysis of over 10 years of surveys from more than 2000 ORBIT students (38% Black, 8.7% Hispanic, 28% White/Asian/Multiracial/Other Women, and 24% White/Asian Men) shows that students felt that the ORBIT increased their intentions to persist in computing. These results were significantly higher for Black women and Black men. In addition, ORBIT students had positive gains in GPA, self-efficacy, computing identity, and commitment to computing, with enhanced outcomes for students who identify as women, Black, Hispanic, Native American, and Pacific Islander/Native Hawaiian.

Target Market(s)

diversity in tech, college faculty in computer science, college students in computer science,

Industry/Entity Type

computer science, tech, higher education

Font styles to use
Sans Serif

Colors
0054AA
0677BA
7BADD7
CADEEF
E8F1F8
0094D4
00A9DD
6FCCEA
C7EBF8
E9F6FB
E54698
E96AAD
F1A4CE
F9D9EA
FCEFF6
A7469A
B969AE
D3A5CF
EDDBEB
F8F0F9
6B429C
8869AF
B7A5CE
E3DAEB
F3F0F8

```html
<!DOCTYPE html>
<html lang="en">
<head>
<meta charset="utf-8">
<title>ORBIT Learning League – Different But Equal Sticker</title>
<link rel="stylesheet" href="https://fonts.googleapis.com/css2?family=League+Spartan:wght@800&family=Jost:wght@400&family=Open+Sans:wght@400&display=swap">
<style>
  :root {
    --paper: #ffffff;
    --navy: #071a4a;
    --royal: #1456a6;
    --white: #ffffff;
    --violet: #6b429c;
    --sky: #11a8dd;
    --magenta: #e54698;
    --blush: #f1a4ce;
    --cobalt: #1356a6;
    --orchid: #d3a5cf;
    --cocoa: #4a3b3d;
    --azure: #1a93d4;
    --mark: #6fccea;
  }
  html, body {
    margin: 0;
    padding: 0;
    width: 1200px;
    height: 903px;
    overflow: hidden;
    background: var(--paper);
  }
  .canvas {
    display: block;
    width: 1200px;
    height: 903px;
  }
  .sticker-body { fill: var(--navy); }
  .headline {
    font-family: "League Spartan", "Futura", sans-serif;
    font-weight: 800;
  }
  .word-but { fill: var(--royal); }
  .word-equal { fill: var(--white); }
  .l-violet { fill: var(--violet); }
  .l-sky { fill: var(--sky); }
  .l-magenta { fill: var(--magenta); }
  .l-blush { fill: var(--blush); }
  .l-cobalt { fill: var(--cobalt); }
  .l-orchid { fill: var(--orchid); }
  .l-cocoa { fill: var(--cocoa); }
  .l-azure { fill: var(--azure); }
  .brand-dot { fill: none; stroke: var(--mark); stroke-width: 3; }
  .brand-name {
    font-family: "Jost", sans-serif;
    font-weight: 400;
    fill: var(--white);
  }
  .brand-tagline {
    font-family: "Open Sans", sans-serif;
    font-weight: 400;
    fill: var(--white);
    letter-spacing: 0.12em;
  }
</style>
</head>
<body>
<svg class="canvas" viewBox="0 0 1200 903" xmlns="http://www.w3.org/2000/svg" role="img" aria-label="Different But Equal sticker for ORBIT Learning League">
  <rect class="sticker-body" x="233" y="70" width="787" height="761" rx="64" ry="64"/>

  <text class="headline word-different" x="317" y="219" font-size="138" textLength="600" lengthAdjust="spacingAndGlyphs"><tspan class="l-violet">D</tspan><tspan class="l-sky">I</tspan><tspan class="l-magenta">F</tspan><tspan class="l-blush">F</tspan><tspan class="l-cobalt">E</tspan><tspan class="l-orchid">R</tspan><tspan class="l-cocoa">E</tspan><tspan class="l-azure">N</tspan><tspan class="l-magenta">T</tspan></text>

  <text class="headline word-but" x="315" y="517" font-size="405" textLength="603" lengthAdjust="spacingAndGlyphs">BUT</text>

  <text class="headline word-equal" x="310" y="670" font-size="192" textLength="623" lengthAdjust="spacingAndGlyphs">EQUAL.</text>

  <g class="brand-lockup">
    <circle class="brand-dot" cx="320" cy="741" r="32"/>
    <text class="brand-name" x="370" y="754" font-size="47" textLength="569" lengthAdjust="spacingAndGlyphs">ORBIT LEARNING LEAGUE</text>
    <text class="brand-tagline" x="369" y="781" font-size="19" textLength="570" lengthAdjust="spacingAndGlyphs">leadership in broadening participation in computing</text>
  </g>
</svg>
</body>
</html>
```